Tide Harbor Finance Business Cards

Looking for a business card for a new mortgage broking business. Name of the business is Tide Harbor Finance. Purpose of the business is to build trust and strong relationships with clients to then assist them with your mortgage lending needs. Most relationships within the business start off as an enquiry, and then can evolve into a 10+ year relationship, servicing clients from purchasing a new home to then upgrading for their family and even then assisting their children with their first home purchase. Business card should communicate financial security and trust.

Target Market(s)

Targeting professional clients who are looking to build a relationship with a knowledgeable mortgage professional

Industry/Entity Type

Finance - Home Loans

Contact Information for Business Card

Peter Colburn, Director, mobile: 0427 903186, email:peter@tideharborfinance.com.au, website: www.tideharborfinance.com.au

Font styles to use
Sans Serif

Requirements
Must have
• On the front: Must have company logo, contact details as above. On the back: slogan, 'full of choices, free of stress', plus listing services offered: home loans, investment loans, first home buyers, refinancing, car finance

```html
<!DOCTYPE html>
<html lang="en">
<head>
<meta charset="utf-8">
<title>Tide Harbor Finance – Business Cards</title>
<link href="https://fonts.googleapis.com/css2?family=Lato:wght@400;700;900&family=Montserrat:wght@500;700;800&display=swap" rel="stylesheet">
<style>
  :root {
    --navy: #0b4e76;
    --navy-deep: #083d5e;
    --orange: #f5a10f;
    --white: #ffffff;
    --stage: #1e1f21;
  }
  * { margin: 0; padding: 0; box-sizing: border-box; }
  html, body { width: 1200px; height: 875px; overflow: hidden; }
  body {
    background: var(--stage);
    font-family: "Lato", sans-serif;
    position: relative;
  }
  .card {
    position: absolute;
    top: 277px;
    width: 560px;
    height: 320px;
    border-radius: 18px;
    overflow: hidden;
  }

  /* Back side */
  .card-back { left: 30px; background: var(--navy); }
  .back-brand {
    position: absolute;
    top: 70px; left: 0; width: 100%;
    display: flex; flex-direction: column; align-items: center; gap: 14px;
  }
  .brand-mark {
    width: 22px; height: 22px; border-radius: 50%;
    background: var(--orange);
  }
  .back-brand .brand-name {
    font-family: "Montserrat", sans-serif;
    font-weight: 700; font-size: 30px; letter-spacing: 2px;
    color: var(--white); text-transform: uppercase;
  }
  .slogan {
    position: absolute; top: 176px; width: 100%;
    text-align: center; font-size: 20px; color: var(--orange);
  }
  .slogan strong { font-weight: 900; }
  .services {
    position: absolute; left: 24px; right: 24px; top: 238px;
    height: 34px; border-radius: 17px; background: var(--white);
    padding: 0 16px;
    display: flex; align-items: center; justify-content: space-between;
    font-size: 10px; letter-spacing: 0.2px; color: var(--navy);
    text-transform: uppercase; white-space: nowrap;
  }
  .services span { flex: none; }
  .services .dot { width: 4px; height: 4px; border-radius: 50%; background: var(--orange); }

  /* Front side */
  .card-front { left: 610px; background: var(--white); }
  .front-band { position: absolute; inset: 0; }
  .front-brand {
    position: absolute; top: 44px; left: 150px;
    display: flex; align-items: center; gap: 14px;
  }
  .front-brand .brand-mark { width: 26px; height: 26px; border-radius: 4px; background: var(--navy); }
  .front-brand .brand-name {
    font-family: "Montserrat", sans-serif;
    font-weight: 700; font-size: 28px; line-height: 1.05;
    color: var(--navy); text-transform: uppercase;
  }
  .person { position: absolute; left: 34px; top: 232px; }
  .person-name {
    font-family: "Montserrat", sans-serif; font-weight: 800;
    font-size: 24px; letter-spacing: 0.5px; color: var(--orange);
  }
  .person-role { font-size: 15px; color: var(--white); text-align: right; margin-top: 2px; }
  .divider {
    position: absolute; left: 284px; top: 200px; width: 1.5px; height: 86px;
    background: var(--orange);
  }
  .contacts {
    position: absolute; left: 300px; top: 204px;
    list-style: none; display: flex; flex-direction: column; gap: 10px;
    font-size: 13px; color: var(--white); white-space: nowrap;
  }
  .contacts li { display: flex; align-items: center; gap: 8px; }
  .contacts svg { width: 12px; height: 12px; flex: none; }
</style>
</head>
<body>

<section class="card card-back" aria-label="Business card, back">
  <div class="back-brand">
    <span class="brand-mark"></span>
    <span class="brand-name">Tide Harbor Finance</span>
  </div>
  <p class="slogan">Full of <strong>Choices</strong>, Free of <strong>Stress</strong></p>
  <p class="services">
    <span>Home Loans</span><span class="dot"></span>
    <span>Investment Loans</span><span class="dot"></span>
    <span>First Home Buyers</span><span class="dot"></span>
    <span>Refinancing</span><span class="dot"></span>
    <span>Car Finance</span>
  </p>
</section>

<section class="card card-front" aria-label="Business card, front">
  <svg class="front-band" viewBox="0 0 560 320" preserveAspectRatio="none" aria-hidden="true">
    <polygon points="0,232 250,160 540,128 540,120 560,120 560,320 0,320" fill="var(--navy)"/>
    <polyline points="0,222 250,150 540,118" fill="none" stroke="var(--orange)" stroke-width="4"/>
    <polyline points="0,212 250,140 528,109 528,101 560,101" fill="none" stroke="var(--navy)" stroke-width="4"/>
  </svg>

  <div class="front-brand">
    <span class="brand-mark"></span>
    <span class="brand-name">Tide Harbor<br>Finance</span>
  </div>

  <div class="person">
    <p class="person-name">PETER COLBURN</p>
    <p class="person-role">Director</p>
  </div>
  <span class="divider"></span>
  <ul class="contacts">
    <li>
      <svg viewBox="0 0 24 24" aria-hidden="true"><path fill="var(--orange)" d="M6.6 10.8a15 15 0 0 0 6.6 6.6l2.2-2.2a1 1 0 0 1 1-.25 11.4 11.4 0 0 0 3.6.57 1 1 0 0 1 1 1V20a1 1 0 0 1-1 1A17 17 0 0 1 3 4a1 1 0 0 1 1-1h3.5a1 1 0 0 1 1 1c0 1.25.2 2.45.57 3.570a1 1 0 0 1-.25 1z"/></svg>
      <span>0427 903186</span>
    </li>
    <li>
      <svg viewBox="0 0 24 24" aria-hidden="true"><path fill="var(--orange)" d="M2 5h20v14H2z"/><path fill="none" stroke="var(--navy)" stroke-width="2" d="M2 5l10 8 10-8"/></svg>
      <span>peter@tideharborfinance.com.au</span>
    </li>
    <li>
      <svg viewBox="0 0 24 24" aria-hidden="true"><circle cx="12" cy="12" r="10" fill="none" stroke="var(--orange)" stroke-width="2.5"/><path fill="none" stroke="var(--orange)" stroke-width="2" d="M2 12h20M12 2c3 3 3 17 0 20M12 2c-3 3-3 17 0 20"/></svg>
      <span>www.tideharborfinance.com.au</span>
    </li>
  </ul>
</section>

</body>
</html>
```